Letterhead design for Sleep Consulting Business

I'm looking for a new letterhead (heading/footer) design for my Sleep Consulting Business, I work with families to help their children improve their sleep.

The heading/footer will used in Microsoft Word Only-to be used for all of my documents such as writing Sleep Plans. I need to utilize as much working space in the document as possible. This will NOT be printed out on paper- it will only be used for heading/footer on microsoft word, then emailed to clients, who may print it at home.

My brand colors:
Dark Blue Hex: 1F2A42
Lighter Blueish Hex: 90BEC9
You're welcome to check out my website for inspiration- it is freshly created with other colors as well, and I love the outcome. www.hollowpinerest.com

Target Market(s)

Tired parents

Font styles to use
Script
Other font styles liked:
• Great Vibe, Lato or Just Another Hand are all used currently for my brand. Open to other options.

Requirements
Must have
• The letterhead (heading/footer) MUST be kept narrow (height-wise), so I have plenty of space on my document, while including important information.

It should look professional on screen, and when printed.

Must include my business name OR logo (Hollow Pine Sleep Consulting), and my email address. Mara@hollowpinerest.com

Website is optional, not required, just if you need to fill in a spot: www.hollowpinerest.com

```html
<!DOCTYPE html>
<html lang="en">
<head>
<meta charset="utf-8">
<title>Hollow Pine Sleep Consulting – Letterhead</title>
<link rel="stylesheet" href="https://fonts.googleapis.com/css2?family=Montserrat:wght@300;400;500&display=swap">
<style>
  :root {
    --navy: #1f2a42;
    --sky: #90bec9;
    --ink: #3a3f4a;
    --muted: #8b909a;
    --rule: #9aa0aa;
    --stage: #aaaaaa;
    --paper: #ffffff;
    --paper-shade: #eef0f3;
  }
  * { box-sizing: border-box; margin: 0; padding: 0; }
  html, body { width: 1200px; height: 1200px; overflow: hidden; }
  body {
    background: var(--stage);
    font-family: "Montserrat", Arial, sans-serif;
    position: relative;
  }
  .letterhead {
    position: absolute;
    left: 197px; top: 30px;
    width: 806px; height: 1140px;
    background: linear-gradient(160deg, var(--paper) 30%, var(--paper-shade) 100%);
    overflow: hidden;
  }
  .header-band { position: absolute; left: 0; top: 0; width: 806px; height: 80px; }
  .brand {
    position: absolute; left: 53px; top: 52px;
    display: flex; align-items: center; gap: 14px;
  }
  .brand-dot { width: 62px; height: 62px; border-radius: 50%; background: var(--navy); }
  .brand-name { font-size: 19px; font-weight: 400; color: var(--navy); letter-spacing: .3px; }

  .recipient { position: absolute; left: 82px; top: 254px; }
  .recipient .label { font-size: 13px; font-weight: 500; letter-spacing: 2px; color: var(--ink); }
  .recipient .name { margin-top: 8px; font-size: 13.5px; font-weight: 500; color: var(--sky); }
  .recipient .line { font-size: 10.5px; font-weight: 300; color: var(--muted); line-height: 18px; }
  .recipient .name + .line { margin-top: 3px; }
  .date { position: absolute; right: 83px; top: 254px; font-size: 11px; color: var(--ink); font-weight: 400; }

  .letter-body { position: absolute; left: 82px; top: 412px; width: 641px; }
  .letter-body p {
    font-size: 11.2px; font-weight: 300; color: var(--muted);
    line-height: 14.3px; text-align: justify; margin-bottom: 14px;
  }

  .signature-mark {
    position: absolute; left: 82px; top: 806px; width: 140px; height: 30px;
    background: linear-gradient(90deg, #d9dce2, #eceef1);
    border-radius: 4px;
  }
  .signatory { position: absolute; left: 80px; top: 848px; }
  .signatory .name { font-size: 12.5px; font-weight: 500; color: var(--ink); }
  .signatory .role { font-size: 10.5px; font-weight: 300; color: var(--muted); margin-top: 2px; }

  .footer {
    position: absolute; left: 56px; right: 56px; top: 1094px;
    display: flex; align-items: center; gap: 12px;
    font-size: 12px; color: var(--navy); font-weight: 400;
  }
  .footer .rule { flex: 1; height: 1px; background: var(--rule); }
  .footer .item { display: flex; align-items: center; gap: 6px; white-space: nowrap; }
  .footer svg { display: block; }
</style>
</head>
<body>
<main class="letterhead">
  <svg class="header-band" viewBox="0 0 700 70" preserveAspectRatio="none" aria-hidden="true">
    <path fill="#1f2a42" d="M0,0 H700 V40 C610,44 520,38 400,24 C300,13 210,11 130,16 C80,20 35,27 0,32 Z"/>
    <path fill="#90bec9" d="M0,38 C60,26 140,18 260,17 C170,20 80,30 0,48 Z"/>
    <path fill="#90bec9" d="M470,40 C560,48 630,49 700,38 V52 C630,62 560,56 470,40 Z"/>
  </svg>

  <div class="brand">
    <span class="brand-dot"></span>
    <span class="brand-name">Hollow Pine Sleep Consulting</span>
  </div>

  <section class="recipient">
    <p class="label">TO</p>
    <p class="name">Colin Fairweather</p>
    <p class="line">Human Resources</p>
    <p class="line">Brightfield Labs</p>
    <p class="line">48 Alder Lane, Westbrook</p>
    <p class="line">ME 04092 USA</p>
  </section>
  <p class="date">Friday, 01/01/2018</p>

  <article class="letter-body">
    <p>Lorem ipsum dolor sit amet, consectetuer adipiscing elit, sed diam nonmmy nibh euismod tincidunt ut laoreet dolore magna aliquam erat volutpat. Ut wisi enim ad minim veniam, quis nostrud exerci tationmcorper suscipit lobortis nisl ut aliquip ex ea commodo consequat. Duis autem vel eum iriure dolor in hendrerit in vulputate velit esse molestie consequat, vel illum dolore eu feugiat nulla facilisis at vero eros et accumsan et iusto odio dignissim qui blandit praesent luptatum zzril delenit augue duis dolore te feugait nulla facilisi.</p>
    <p>Nam liber tempor cum soluta nobis eleifend option congue nihil imprdiet doming id quod mazim placerat facer possim assum. Typi non habent claritatem insitam;</p>
    <p>Est usus legentis in iis qui facit eorum claritatem.</p>
    <p>Investigationes demonstraverunt lectores legere me lius quod ii legunt saepius. Claritas est etiam processus dynamicus, qui sequitur mutationem consuetudium lectorum. Mirum est notare quam littera gothica, quam nunc putamus parum claram, anteposuerit litterarum formas humanitatis per seacula quarta decima et quinta decima. Eodem modo typi, qui nunc nobis videntur parum clari, fiant sollemnes in futurum.</p>
    <p>consectetuer adipiscing elit, sed diam nonummy nibh euismod tincidunt ut laoreet dolore magna aliquam erat volutpat. Ut wisi enim ad minim veniam, quis nostrud exerci tation ullamcorper suscipit lobortis nisl ut aliquip ex ea commodo consequat. Duis autem vel eum iriure dolor in hendrerit in vulputate velit esse molestie consequat, vel illum dolore eu feugiat nulla facilisis at vero eros et accumsan et iusto odio dignissim qui blandit praesent luptatum zzril delenit augue duis dolore te feugait nulla facilisi.</p>
    <p>Nam liber tempor cum soluta nobis eleifend option congue nihil imperdiet .</p>
  </article>

  <div class="signature-mark" role="img" aria-label="Handwritten signature of Peter Lansing"></div>
  <div class="signatory">
    <p class="name">Peter Lansing</p>
    <p class="role">Managing Director</p>
  </div>

  <footer class="footer">
    <span class="rule"></span>
    <span class="item">
      <svg width="11" height="8" viewBox="0 0 11 8" aria-hidden="true"><rect x="0.5" y="0.5" width="10" height="7" fill="#90bec9" stroke="#1f2a42" stroke-width=".6"/><path d="M0.5,0.5 L5.5,4.5 L10.5,0.5" fill="none" stroke="#1f2a42" stroke-width=".6"/></svg>
      Mara@hollowpinerest.com
    </span>
    <span class="item">
      <svg width="11" height="11" viewBox="0 0 11 11" aria-hidden="true"><circle cx="5.5" cy="5.5" r="5" fill="#90bec9"/><circle cx="5.5" cy="5.5" r="5" fill="none" stroke="#1f2a42" stroke-width=".6"/><path d="M0.5,5.5 H10.5 M5.5,0.5 V10.5" stroke="#1f2a42" stroke-width=".6"/></svg>
      www.hollowpinerest.com
    </span>
    <span class="rule"></span>
  </footer>
</main>
</body>
</html>
```